St Louis Electrician Needing a Business Card Design!!

We are a St Louis based electrical contracting firm that needs help designing a business card. We have a logo and I have another image that I would like to incorporate. Open to ideas..Thanks!!

Industry/Entity Type

Business

Requirements
Must have
• there are two downloads...one is the logo and the other is what i was wanting coming off the logo...the light rays. Like the logo with the blue background...Was thinking the whole card would be that color blue.
Should not have
• No lightning bolts

```html
<!DOCTYPE html>
<html lang="en">
<head>
<meta charset="utf-8">
<title>Keystone Current Co. – Business Card</title>
<link rel="stylesheet" href="https://fonts.googleapis.com/css2?family=Source+Sans+3:wght@400;600&display=swap">
<style>
  :root {
    --backdrop: #2b2a29;
    --card: #161616;
    --card-edge: #1f1f1f;
    --brand-blue: #1b63c6;
    --text-light: #f2f2f2;
    --text-muted: #cfcfcf;
  }
  * { box-sizing: border-box; margin: 0; padding: 0; }
  html, body {
    width: 1200px; height: 844px; overflow: hidden;
    background: var(--backdrop);
    font-family: "Source Sans 3", "Myriad Pro", Arial, sans-serif;
  }
  .stage {
    width: 1200px; height: 844px;
    display: flex; align-items: center; justify-content: center; gap: 48px;
  }
  .card {
    position: relative;
    width: 540px; height: 309px;
    background: linear-gradient(160deg, var(--card-edge), var(--card));
    border-radius: 3px;
    box-shadow: 0 10px 30px rgba(0,0,0,.45);
    overflow: hidden;
  }
  .wordmark {
    display: flex; align-items: center; gap: 10px;
    color: var(--brand-blue);
    font-weight: 400;
    white-space: nowrap;
  }
  .wordmark-dot {
    width: 12px; height: 12px; border-radius: 50%;
    background: var(--brand-blue);
  }
  .card-front .wordmark {
    position: absolute; top: 78px; left: 150px;
    font-size: 34px;
  }
  .card-back .wordmark {
    position: absolute; top: 50%; left: 50%;
    transform: translate(-50%, -50%);
    font-size: 40px;
  }
  .identity {
    position: absolute; left: 34px; bottom: 30px;
    color: var(--text-light);
    font-size: 15px; line-height: 1.15;
  }
  .identity .person-name {
    color: var(--brand-blue);
    font-size: 22px; margin-bottom: 2px;
  }
  .identity .person-role { margin-bottom: 14px; }
  .contact-list {
    position: absolute; right: 22px; top: 150px;
    list-style: none;
    color: var(--text-light);
    font-size: 14.5px; line-height: 1.45;
    text-align: right;
  }
  .contact-list li {
    display: flex; align-items: center; justify-content: flex-end; gap: 8px;
  }
  .contact-icon { width: 11px; height: 11px; flex: none; }
  .contact-icon path, .contact-icon rect { fill: none; stroke: var(--brand-blue); stroke-width: 2; }
</style>
</head>
<body>
<main class="stage">
  <section class="card card-front">
    <div class="wordmark"><span class="wordmark-dot"></span>Keystone Current Co.</div>

    <ul class="contact-list">
      <li>(314)-555-0182
        <svg class="contact-icon" viewBox="0 0 12 12" aria-hidden="true"><path d="M2 1.5 L4.5 1.5 L5.5 4 L4 5 Q5 7.5 7 8 L8 6.5 L10.5 7.5 L10.5 10 Q4 11 1.5 4 Z"/></svg>
      </li>
      <li>hello@keystonecurrent.com
        <svg class="contact-icon" viewBox="0 0 12 12" aria-hidden="true"><rect x="1" y="2.5" width="10" height="7"/><path d="M1 2.5 L6 6.5 L11 2.5"/></svg>
      </li>
      <li>www.keystonecurrent.com
        <svg class="contact-icon" viewBox="0 0 12 12" aria-hidden="true"><path d="M5 7 L7 5 M4 5.5 L2.5 7 Q1 9 3 10 Q4.5 10.5 6 9 L6.5 8 M8 6.5 L9.5 5 Q11 3 9 2 Q7.5 1.5 6 3 L5.5 4"/></svg>
      </li>
    </ul>

    <div class="identity">
      <p class="person-name">Daniel Reeves</p>
      <p class="person-role">Managing Director</p>
      <p>4410 Delmar Blvd, Suite 2</p>
      <p>St Louis, MO 63108</p>
    </div>
  </section>

  <section class="card card-back">
    <div class="wordmark"><span class="wordmark-dot"></span>Keystone Current Co.</div>
  </section>
</main>
</body>
</html>
```